Arvo 7 Detection Wheel

We need a professional **framework wheel diagram** designed for our detection dog training manual.

Our business is **Arvo 7 Dog Training**, and this graphic represents our **Detection Training Model**.

Please use the **attached reference images** as a guide for the structure and layout of the wheel.

### What we need

1. **Full wheel graphic**

* Clean circular framework wheel
* Similar structure to the attached example
* Clear sections and text
* Professional training manual style
* Transparent background

2. **Individual segment pieces**

We also need the **inner sections broken into separate pieces** (like the second reference image).

This will allow us to place each section on different pages of the manual when explaining the concepts.

Each piece should look like a **slice of the wheel**.

### Style

The design should look:

• Professional
• Clean and modern
• Structured and easy to read
• Suitable for a training manual

Avoid cartoon styles or clipart.

### Colours

Please use our brand colour palette (see attached image):

* Dark navy blue
* Steel blue
* Light blue
* White
* Light grey
* Dark grey

### Files required

Final files must include:

* Vector files (AI or EPS)
* Transparent PNG
* High-resolution PDF

Please also provide **each segment exported individually**

```html
<!DOCTYPE html>
<html lang="en">
<head>
<meta charset="utf-8">
<title>Arvo 7 Detection Wheel</title>
<link href="https://fonts.googleapis.com/css2?family=Bebas+Neue&family=Montserrat:wght@500;600&display=swap" rel="stylesheet">
<style>
  :root {
    --ring-grey: #595959;
    --ring-edge: #2e2e2e;
    --navy: #2a4560;
    --steel: #5e9ab5;
    --midnight: #1c2533;
    --divider: #222a33;
    --divider-soft: #2f3642;
    --centre: #f4f4f4;
    --text-light: #f2f2f2;
    --text-dark: #1c2533;
    --page: #ffffff;
  }
  html, body {
    margin: 0;
    padding: 0;
    width: 1200px;
    height: 1200px;
    overflow: hidden;
    background: var(--page);
  }
  .wheel {
    display: block;
    width: 1200px;
    height: 1200px;
  }
  .ring-label {
    font-family: "Montserrat", sans-serif;
    font-weight: 500;
    font-size: 36px;
    fill: var(--text-light);
  }
  .area-label {
    font-family: "Montserrat", sans-serif;
    font-weight: 600;
    font-size: 28px;
    letter-spacing: 1px;
    fill: var(--text-light);
    text-anchor: middle;
  }
  .pillar-label {
    font-family: "Montserrat", sans-serif;
    font-weight: 500;
    font-size: 19px;
    letter-spacing: 0.5px;
    fill: var(--text-light);
    text-anchor: middle;
  }
  .core-title {
    font-family: "Bebas Neue", sans-serif;
    font-size: 56px;
    fill: var(--text-dark);
    text-anchor: middle;
  }
</style>
</head>
<body>
<svg class="wheel" viewBox="0 0 1200 1200" xmlns="http://www.w3.org/2000/svg" role="img" aria-label="Detection Capabilities framework wheel">
  <defs>
    <path id="outer-top-arc" d="M 59 600 A 541 541 0 0 1 1141 600"/>
    <path id="outer-bottom-arc" d="M 31 600 A 569 569 0 0 0 1169 600"/>
    <path id="inner-top-arc" d="M 304 600 A 296 296 0 0 1 896 600"/>
    <path id="inner-bottom-arc" d="M 278 600 A 322 322 0 0 0 922 600"/>
  </defs>

  <!-- Outer capability ring -->
  <g class="outer-ring">
    <circle cx="600" cy="600" r="582" fill="var(--ring-grey)" stroke="var(--ring-edge)" stroke-width="3"/>
    <circle cx="600" cy="600" r="528" fill="var(--navy)" stroke="var(--ring-edge)" stroke-width="2"/>
  </g>

  <!-- Area dividers -->
  <g class="area-dividers" stroke="var(--divider)" stroke-width="2">
    <line x1="600" y1="600" x2="600" y2="72"/>
    <line x1="600" y1="600" x2="1011.6" y2="188.4"/>
    <line x1="600" y1="600" x2="188.4" y2="188.4"/>
    <line x1="600" y1="600" x2="188.4" y2="1011.6"/>
    <line x1="600" y1="600" x2="1011.6" y2="1011.6"/>
    <line x1="600" y1="600" x2="1182" y2="600"/>
    <line x1="600" y1="600" x2="18" y2="600"/>
    <line x1="600" y1="600" x2="600" y2="1182"/>
    <line x1="600" y1="600" x2="1087.8" y2="397.9"/>
  </g>

  <!-- Outer ring titles -->
  <text class="ring-label">
    <textPath href="#outer-top-arc" startOffset="50%" text-anchor="middle" textLength="780" lengthAdjust="spacing">OPERATIONAL CAPABILITY AREA</textPath>
  </text>
  <text class="ring-label">
    <textPath href="#outer-bottom-arc" startOffset="50%" text-anchor="middle" textLength="790" lengthAdjust="spacing">OPERATIONAL CAPABILITY AREA</textPath>
  </text>

  <!-- Operational areas -->
  <g class="area-labels">
    <text class="area-label" x="441" y="215">DEVELOPMENT</text>
    <text class="area-label" x="761" y="215">DISTRACTIONS</text>
    <text class="area-label" x="955" y="376">BEHAVIOUR</text>
    <text class="area-label" x="1025" y="530">HANDLER</text>
    <text class="area-label" x="983" y="785">TARGET</text>
    <text class="area-label" x="987" y="818">ODOUR</text>
    <text class="area-label" x="770" y="1009">SEARCH METHOD</text>
    <text class="area-label" x="428" y="1010">REINFORCEMENT</text>
    <text class="area-label" x="213" y="801">DEPLOYMENT</text>
    <text class="area-label" x="217" y="418">INTEGRITY</text>
  </g>

  <!-- Inner capability ring -->
  <circle class="inner-ring" cx="600" cy="600" r="335" fill="var(--ring-grey)" stroke="var(--ring-edge)" stroke-width="2"/>
  <text class="ring-label">
    <textPath href="#inner-top-arc" startOffset="50%" text-anchor="middle" textLength="830" lengthAdjust="spacing">OPERATIONAL CAPABILITY AREA</textPath>
  </text>
  <text class="ring-label">
    <textPath href="#inner-bottom-arc" startOffset="50%" text-anchor="middle" textLength="700" lengthAdjust="spacing">HANDLER FOUNDATIONS</textPath>
  </text>

  <!-- Dog pillars (upper) and handler foundations (lower) -->
  <g class="pillars">
    <path d="M 318 600 A 282 282 0 0 1 882 600 Z" fill="var(--steel)"/>
    <path d="M 318 600 A 282 282 0 0 0 882 600 Z" fill="var(--midnight)"/>
    <circle cx="600" cy="600" r="282" fill="none" stroke="var(--ring-edge)" stroke-width="2"/>
    <g stroke="var(--divider)" stroke-width="2">
      <line x1="600" y1="600" x2="360.9" y2="450.6"/>
      <line x1="600" y1="600" x2="499" y2="336.7"/>
      <line x1="600" y1="600" x2="701" y2="336.7"/>
      <line x1="600" y1="600" x2="839.1" y2="450.6"/>
    </g>
    <g stroke="var(--divider-soft)" stroke-width="2">
      <line x1="600" y1="600" x2="411.3" y2="809.5"/>
      <line x1="600" y1="600" x2="600" y2="882"/>
      <line x1="600" y1="600" x2="788.7" y2="809.5"/>
    </g>
  </g>

  <g class="pillar-labels">
    <text class="pillar-label" x="409" y="550">GENETIC</text>
    <text class="pillar-label" x="409" y="574">SUITABILITY</text>
    <text class="pillar-label" x="472" y="428">HEALTH&amp;</text>
    <text class="pillar-label" x="472" y="450">PHYSICAL</text>
    <text class="pillar-label" x="472" y="473">WELLBEING</text>
    <text class="pillar-label" x="600" y="363">ENGAGEMENT</text>
    <text class="pillar-label" x="602" y="386">RELATIONSHIP</text>
    <text class="pillar-label" x="740" y="437">REWARD</text>
    <text class="pillar-label" x="740" y="462">VALUE</text>
    <text class="pillar-label" x="792" y="549">AROUSAL</text>
    <text class="pillar-label" x="792" y="572">REGULATION</text>
    <text class="pillar-label" x="411" y="664">DOG</text>
    <text class="pillar-label" x="412" y="689">SAFETY</text>
    <text class="pillar-label" x="522" y="783">SEARCH</text>
    <text class="pillar-label" x="522" y="808">COVERAGE</text>
    <text class="pillar-label" x="684" y="775">MINIMAL</text>
    <text class="pillar-label" x="684" y="797">NECESSARY</text>
    <text class="pillar-label" x="684" y="819">INVOLVEMENT</text>
    <text class="pillar-label" x="787" y="664">READ</text>
    <text class="pillar-label" x="789" y="689">THE DOG</text>
  </g>

  <!-- Core -->
  <g class="core">
    <circle cx="600" cy="600" r="110.5" fill="var(--centre)"/>
    <text class="core-title" x="600" y="603" textLength="196" lengthAdjust="spacingAndGlyphs">DETECTION</text>
    <text class="core-title" x="600" y="644" textLength="196" lengthAdjust="spacingAndGlyphs">CAPABILITIES</text>
  </g>
</svg>
</body>
</html>
```